Velvet Heron Website

We need a website for our software / project management services company based in South Africa called "Velvet Heron". We provide professional services to high value clients in the public and private sectors.

The website must present a highly professional company that exudes quality and confidence.

The theme should be a highly professional subdued look with a fairly limited palette. The neutral tone should be slightly offset with the colours from the company logo. The website should not look dead though, and subtle colour highligting should provide a fresh vibrant feel.

Refer to the current website for general content (www.velvetheron-example.co.za) that may be used. We would also like to make use of social integration and google maps.
Updates

Thanks to all the designers that have participated so far and to those that are cooking something up at this very minute :-)

We have received a lot of designs with elements that we absolutely love. So now the hard work of refining these designs can begin.

We'll try and provide feedback on every design received so far ... and await the beautiful designs that we haven't received yet :-)

Good Luck!

Reason: After careful consideration we are extending the deadline to make small revisions to some of the designs and to select the top three designs. Thank you for everyone who has made a contribution so far - we have several designs that we like and selecting the best one is proving to be difficult :-)

Target Market(s)

The company deals mostly with other businesses, so mostly B2B.

Industry/Entity Type

Software

Requirements
Nice to have
• Social integration

```html
<!DOCTYPE html>
<html lang="en">
<head>
<meta charset="utf-8">
<title>Velvet Heron</title>
<link href="https://fonts.googleapis.com/css2?family=Arimo:wght@400;700&family=Noto+Sans:wght@400&family=PT+Sans:wght@700&display=swap" rel="stylesheet">
<style>
:root{
  --green:#7cbb3c;
  --green-light:#93cd4f;
  --green-dark:#5e9a26;
  --ink:#222;
  --text:#555;
  --muted:#777;
  --accent-red:#8b1a1a;
  --accent-green:#5c8f27;
  --line:#bbb;
  --panel:#f1f1f1;
  --white:#fff;
}
*{box-sizing:border-box;margin:0;padding:0}
html,body{width:833px;height:1200px;overflow:hidden;background:var(--white)}
body{position:relative;font-family:"Arimo",Arial,sans-serif;color:var(--text)}
.abs{position:absolute}

.site-header{left:0;top:0;width:833px;height:90px;background:linear-gradient(#fff,#f3f3f3)}
.brand{left:36px;top:28px;display:flex;align-items:center;gap:10px}
.brand-mark{width:40px;height:40px;border-radius:50%;background:var(--green)}
.brand-name{font-family:"PT Sans",Arial,sans-serif;font-weight:700;font-size:38px;color:#6b6b6b;letter-spacing:.5px}
.search{left:675px;top:46px;width:138px;height:22px;border:1px solid #bbb;border-radius:4px;background:#fff;box-shadow:inset 0 1px 2px rgba(0,0,0,.1);font-size:10px;font-style:italic;color:#999;padding:4px 8px}
.search svg{position:absolute;right:5px;top:4px}

.hero{left:0;top:90px;width:833px;height:288px;background:linear-gradient(var(--green-light),var(--green) 60%,#6fae32)}
.hero-bar{left:0;top:378px;width:833px;height:10px;background:linear-gradient(var(--green),var(--green-dark))}
.hero-photo{left:34px;top:108px;width:479px;height:251px;border:3px solid #fff;border-radius:6px;background:linear-gradient(135deg,#c9c3bb,#8f8a86 45%,#d7d4cf);box-shadow:0 1px 4px rgba(0,0,0,.3)}
.slider-btn{width:22px;height:22px;border-radius:50%;background:#fff;box-shadow:0 1px 3px rgba(0,0,0,.4);display:flex;align-items:center;justify-content:center}
.hero-copy{left:573px;top:136px;width:240px;font-family:"Noto Sans",Arial,sans-serif;font-size:12.4px;line-height:20px;color:#fff}
.btn-read{left:645px;top:303px;width:93px;height:36px;border:2px solid #fff;border-radius:5px;background:linear-gradient(#fff,#e6e6e6);font-size:12px;color:#333;display:flex;align-items:center;justify-content:center;box-shadow:0 1px 3px rgba(0,0,0,.25)}

.nav-band{left:0;top:388px;width:833px;height:50px;background:linear-gradient(#d6d6d6,#a9a9a9 50%,#d9d9d9)}
.nav{left:37px;top:395px;width:777px;height:37px;background:linear-gradient(#fff,#f0f0f0);border-radius:3px;font-size:11.5px;color:var(--ink)}
.nav a{position:absolute;top:0;color:inherit;text-decoration:none;height:37px;line-height:39px;white-space:nowrap}
.nav a.current{left:21px;width:69px;text-align:center;background:linear-gradient(#fff,#d2d2d2)}

.service-col h2{font-size:12.5px;font-weight:400;color:var(--ink);padding-bottom:6px;border-bottom:1px dotted var(--line);display:block;width:155px;white-space:nowrap;margin-bottom:15px}
.service-col ul{list-style:none}
.service-col li{font-size:11px;color:var(--text);height:25px;padding-left:14px;position:relative;white-space:nowrap}
.service-col li::before{content:"›";position:absolute;left:0;top:-2px;color:#999;font-size:13px}

.welcome-band{left:0;top:677px;width:360px;height:28px;background:linear-gradient(90deg,#f1f1f1,#fff)}
.welcome-title{left:52px;top:684px;font-size:12px;color:var(--ink);padding-bottom:7px;border-bottom:1px dotted var(--line);width:173px;white-space:nowrap}
.welcome-title span{color:var(--accent-green)}
.welcome-line{left:0;top:704px;width:833px;height:1px;background:#e5e5e5}
.globe-art{left:52px;top:714px;width:226px;height:150px;background:radial-gradient(circle at 45% 40%,#6aaee6,#cfe3f3 45%,#fff 70%)}
.welcome-copy{left:297px;top:737px;width:520px;font-size:10.7px;line-height:17.6px;color:var(--text)}
.link-more{font-size:10.5px;color:var(--accent-red);text-decoration:none}

.card{top:907px;width:247px;height:170px;background:linear-gradient(#fafafa,#ececec);border:1px solid #ddd;box-shadow:0 1px 4px rgba(0,0,0,.2)}
.card h3{font-size:12.5px;font-weight:400;color:var(--ink);padding:10px 20px 0;height:33px}
.card-body{position:absolute;left:0;top:33px;width:100%;height:136px;background:linear-gradient(#e3e3e3,#f4f4f4)}
.card p{font-size:9.3px;line-height:17.5px;color:#333}
.client{position:absolute;font-weight:700;font-size:12px;white-space:nowrap}

.footer{left:0;top:1102px;width:833px;height:98px;background:linear-gradient(#d9d9d9,#f6f6f6 40%,#fff)}
.footer-links{left:110px;top:1130px;font-size:9.5px;color:#444}
.footer-links span{color:#999;margin:0 6px}
.copyright{left:159px;top:1161px;font-size:9.5px;color:#444}
.social-label{left:676px;top:1119px;font-size:9.5px;color:#444}
.social{left:674px;top:1148px;display:flex;gap:9px}
.social i{width:18px;height:18px;border-radius:2px;display:block}
</style>
</head>
<body>

<header class="abs site-header">
  <div class="abs brand"><span class="brand-mark"></span><span class="brand-name">Velvet Heron</span></div>
  <div class="abs search">Search...
    <svg width="12" height="12" viewBox="0 0 12 12"><circle cx="5" cy="5" r="3.5" fill="none" stroke="#2a7fd4" stroke-width="1.6"/><line x1="7.5" y1="7.5" x2="11" y2="11" stroke="#2a7fd4" stroke-width="2"/></svg>
  </div>
</header>

<section class="abs hero"></section>
<div class="abs hero-bar"></div>
<div class="abs hero-photo" role="img" aria-label="Photo of a team working together at computer screens"></div>
<div class="abs slider-btn" style="left:5px;top:221px"><svg width="8" height="8" viewBox="0 0 8 8"><path d="M5 1L2 4l3 3" fill="none" stroke="#333" stroke-width="1.6"/></svg></div>
<div class="abs slider-btn" style="left:523px;top:217px"><svg width="8" height="8" viewBox="0 0 8 8"><path d="M3 1l3 3-3 3" fill="none" stroke="#333" stroke-width="1.6"/></svg></div>
<p class="abs hero-copy">Lorem ipsum dolor sit amet, adipiscing elit. Nam nibh. Lorem ipsum dolor sit amet, consectetuer adipiscing .Lorem ipsum dolor sit amet, consectetuer adipiscing elit. Nam nibh. Lorem ipsum dolor sit amet, consectetuer adipiscing . Lorem ipsum dolor sit amet.</p>
<a class="abs btn-read">READ MORE</a>

<div class="abs nav-band"></div>
<nav class="abs nav">
  <a class="current">HOME</a>
  <a style="left:108px">ABOUT US</a>
  <a style="left:202px">SOFTWARE DEVELOPMENT</a>
  <a style="left:386px">IT SERVICES</a>
  <a style="left:493px">BLOG</a>
  <a style="left:562px">CONTACT US</a>
</nav>

<section class="abs service-col" style="left:34px;top:466px">
  <h2 style="margin-left:4px">SOFTWARE DEVELOPMENT</h2>
  <ul><li>Search Engine Optimization (SEO)</li><li>Pay per click Management (PPC)</li><li>Social Media Management (SMM)</li><li>Ecommerce Solutions</li><li>Content Management Systems (CMS)</li><li>Interactive Agency Outsourcing</li></ul>
</section>
<section class="abs service-col" style="left:318px;top:466px">
  <h2 style="margin-left:2px">PROJECT MANAGEMENT</h2>
  <ul><li>Custom Application Development</li><li>Product Development</li><li>PortalDesk Development</li><li>Independent Software Testing</li><li>Mobile Development</li><li>Managed Services</li></ul>
</section>
<section class="abs service-col" style="left:611px;top:466px">
  <h2 style="margin-left:-4px">WEB DEVELOPMENT</h2>
  <ul><li>Portals &amp; Collaboration</li><li>Cloud Computing Solutions</li><li>On Demand Software Testing</li><li>Business Process Outsourcing (BPO)</li><li>CIO Advisory</li><li>Staff Augmentation</li></ul>
</section>

<div class="abs welcome-band"></div>
<div class="abs welcome-line"></div>
<h2 class="abs welcome-title" style="font-weight:400">WELCOME TO <span>VELVET HERON</span></h2>
<div class="abs globe-art" role="img" aria-label="Illustration of a globe connected to computer mice"></div>
<div class="abs welcome-copy">
  <p>Lorem ipsum dolor sit amet, adipiscing elit. Nam nibh. Lorem ipsum dolor sit amet, consectetuer adipiscing .Lorem ipsum dolor sit amet, consectetuer adipiscing elit. Nam nibh. Lorem ipsum dolor sit amet, consectetuer adipiscing .Lorem ipsum dolor sit amet.Lorem ipsum dolor sit amet, adipiscing elit. Nam nibh. Lorem ipsum dolor sit amet, consectetuer adipiscing .Lorem ipsum dolor sit amet, consectetuer adipiscing elit. Nam nibh. Lorem ipsum dolor sit amet, consectetuer adipiscing .Lorem ipsum dolor sit amet.</p>
  <a class="link-more" style="display:inline-block;margin:6px 0 0 5px">VIEW MORE</a>
</div>

<section class="abs card" style="left:14px">
  <h3>RECENT PROJECTS</h3>
  <svg class="abs" style="left:212px;top:12px" width="28" height="10" viewBox="0 0 28 10"><path d="M6 1L2 5l4 4M20 1l4 4-4 4" fill="none" stroke="#555" stroke-width="1.8"/></svg>
  <div class="card-body">
    <div class="abs" role="img" aria-label="Software development cycle diagram" style="left:12px;top:16px;width:104px;height:98px;background:#fff;border:1px solid #999;background-image:radial-gradient(circle,#fff 25%,#7db2d9 27%,#8fc46a 45%,#fff 47%)"></div>
    <p class="abs" style="left:129px;top:26px;width:118px">Lorem ipsum dolor sit amet, consectetuer adipiscing elit. Nam nibh. Lorem ipsum dolor sit amet.</p>
    <a class="abs link-more" style="left:131px;top:102px;font-size:9.5px">View more</a>
  </div>
</section>

<section class="abs card" style="left:294px">
  <h3 style="padding-left:18px">TESTIMONIALS</h3>
  <div class="card-body">
    <div class="abs" role="img" aria-label="Portrait of the client giving the testimonial" style="left:8px;top:18px;width:66px;height:66px;border:2px solid #fff;background:linear-gradient(#d8d2cc,#b59f8e);box-shadow:0 0 2px rgba(0,0,0,.4)"></div>
    <p class="abs" style="left:85px;top:14px;color:var(--accent-green)">11 Jan 2012</p>
    <p class="abs" style="left:87px;top:36px;width:160px">Lorem ipsum dolor sit amet, consectetuer adipiscing elit. Nam nibh. Lorem ipsum dolor sit amet.</p>
    <a class="abs link-more" style="left:88px;top:96px;font-size:9.5px">View more</a>
  </div>
</section>

<section class="abs card" style="left:574px">
  <h3>CLIENTS</h3>
  <div class="card-body">
    <span class="client" style="left:22px;top:22px;color:#333">Brightforge</span>
    <span class="client" style="left:140px;top:22px;color:#333">Lumen Analytics</span>
    <span class="client" style="left:32px;top:56px;color:#c8302c">Kestrel</span>
    <span class="client" style="left:140px;top:58px;color:#4d8fa3">Norvale</span>
    <span class="client" style="left:26px;top:94px;color:#2a55b0">Calderon</span>
  </div>
</section>

<footer class="abs footer"></footer>
<div class="abs footer-links">Privacy Policy<span>|</span>Partners<span>|</span>Terms &amp; Conditions<span>|</span> Contact<span>|</span>Sitemap</div>
<div class="abs copyright">Copyright © 2012 Velvet Heron,&nbsp; All rights reserved</div>
<div class="abs social-label">Connect with us :</div>
<div class="abs social">
  <i style="background:#3b5a9a" aria-label="Social network 1"></i>
  <i style="background:#3fa9d9" aria-label="Social network 2"></i>
  <i style="background:#f08a24" aria-label="News feed"></i>
  <i style="background:#1f78b4" aria-label="Social network 3"></i>
  <i style="background:#2d6aa3" aria-label="Social network 4"></i>
</div>

</body>
</html>
```